Contemporary Business Card Design for Management Consulting Firm
M.J. Ortwin Consulting Group, LLC
Cutting-Edge
Dr. Maren J. Ortwin
Transformation Consultant
do not include an address
dr_mj_ortwin@quillpost.com

```html
<!DOCTYPE html>
<html lang="en">
<head>
<meta charset="utf-8">
<title>M.J. Ortwin Consulting Group, LLC — Stationery</title>
<link rel="stylesheet" href="https://fonts.googleapis.com/css2?family=Arimo:wght@400;700&display=swap">
<style>
  :root{
    --backdrop:#a9abad;
    --paper:#ffffff;
    --lime:#b5cf2f;
    --lime-soft:#e4ecc4;
    --grey-soft:#e9eaea;
    --navy:#1d3b7a;
    --ink:#3d4a5c;
    --charcoal:#4a4b4d;
    --charcoal-deep:#2e2f31;
  }
  *{box-sizing:border-box;margin:0;padding:0}
  html,body{width:1200px;height:754px;overflow:hidden}
  body{background:var(--backdrop);font-family:"Arimo",Arial,sans-serif;position:relative}

  .sheet{position:absolute;background:var(--paper);box-shadow:2px 3px 8px rgba(0,0,0,.28)}

  .brand{color:var(--navy);font-weight:700;display:flex;align-items:center;gap:6px;line-height:1.1}
  .brand__dot{flex:none;width:10px;height:10px;border-radius:50%;background:var(--lime)}
  .tagline{font-size:4.5px;letter-spacing:.3px;color:var(--navy);text-transform:uppercase;margin-top:3px}

  /* Letterhead */
  .letterhead{left:96px;top:89px;width:444px;height:607px}
  .letterhead .brand{position:absolute;left:30px;top:30px;font-size:15px;width:190px}
  .letterhead .tagline{position:absolute;left:30px;top:72px;font-size:5px}
  .letterhead__art{position:absolute;left:0;right:0;bottom:0;height:190px;
    background:linear-gradient(170deg,rgba(255,255,255,0) 20%,var(--lime-soft) 55%,var(--grey-soft) 100%)}
  .contact{position:absolute;left:17px;bottom:36px;font-size:7px;line-height:10px;color:var(--ink)}
  .contact span{color:#7a8f1a}

  /* Business cards */
  .card{width:182px;height:106px;border-radius:8px}
  .card--front{left:571px;top:89px;width:187px;height:120px}
  .card--front .brand{position:absolute;left:12px;top:10px;font-size:8px;width:160px}
  .card--front .tagline{position:absolute;left:12px;top:38px;font-size:3.5px}
  .card__person{position:absolute;left:60px;top:58px;font-size:6px;line-height:8.5px;color:var(--ink)}
  .card__person strong{color:var(--navy);font-size:7px}
  .card__lines{position:absolute;left:12px;top:80px;font-size:5px;line-height:7.5px;color:var(--ink)}

  .card--white{left:828px;top:144px;width:180px;height:103px}
  .card--lime{left:629px;top:221px;width:180px;height:103px;background:var(--lime)}
  .card--dark{left:854px;top:276px;width:185px;height:103px;
    background:linear-gradient(160deg,var(--charcoal) 0%,var(--charcoal-deep) 100%)}
  .card--white .brand,.card--lime .brand,.card--dark .brand{
    position:absolute;left:0;right:0;top:0;bottom:0;justify-content:center;font-size:9.5px;text-align:center}
  .card--lime .brand{color:#fff}
  .card--lime .brand__dot{background:#fff}
  .card--dark .brand{color:#fff}

  /* Envelope */
  .envelope{left:576px;top:384px;width:461px;height:317px;overflow:hidden}
  .envelope__flap{position:absolute;left:0;top:0;width:100%;height:84px;background:var(--lime);
    display:flex;align-items:center;justify-content:center}
  .envelope__flap .brand{color:#fff;font-size:11px}
  .envelope__flap .brand__dot{background:#fff}
  .envelope .brand--return{position:absolute;left:20px;top:112px;font-size:10px;width:210px}
  .envelope .tagline{position:absolute;left:20px;top:146px;font-size:4px}
  .envelope__art{position:absolute;left:150px;right:0;bottom:0;height:130px;
    background:linear-gradient(165deg,rgba(255,255,255,0) 15%,var(--lime-soft) 60%,var(--grey-soft) 100%)}
</style>
</head>
<body>

<section class="sheet letterhead">
  <div class="brand"><span class="brand__dot"></span>M.J. Ortwin Consulting Group, LLC</div>
  <p class="tagline">Strategy Management Transformation Growth Solutions</p>
  <div class="letterhead__art" role="img" aria-label="Faint decorative bridge artwork in pale lime and grey"></div>
  <p class="contact"><span>Cell:</span> 555-014-2270<br><span>Fax:</span> 555-014-9385<br><span>Email:</span> dr_mj_ortwin@quillpost.com</p>
</section>

<section class="sheet card card--front">
  <div class="brand"><span class="brand__dot"></span>M.J. Ortwin Consulting Group, LLC</div>
  <p class="tagline">Strategy Management Transformation Growth Solutions</p>
  <p class="card__person"><strong>Dr. Maren J. Ortwin</strong><br>Transformation Consultant</p>
  <p class="card__lines">C: 555-014-2270<br>F: 555-014-9385<br>E: dr_mj_ortwin@quillpost.com</p>
</section>

<section class="sheet card card--white">
  <div class="brand"><span class="brand__dot"></span>M.J. Ortwin Consulting Group, LLC</div>
</section>

<section class="sheet card card--lime">
  <div class="brand"><span class="brand__dot"></span>M.J. Ortwin Consulting Group, LLC</div>
</section>

<section class="sheet card card--dark">
  <div class="brand"><span class="brand__dot"></span>M.J. Ortwin Consulting Group, LLC</div>
</section>

<section class="sheet envelope">
  <div class="envelope__flap"><div class="brand"><span class="brand__dot"></span>M.J. Ortwin Consulting Group, LLC</div></div>
  <div class="brand brand--return"><span class="brand__dot"></span>M.J. Ortwin Consulting Group, LLC</div>
  <p class="tagline">Strategy Management Transformation Growth Solutions</p>
  <div class="envelope__art" role="img" aria-label="Faint decorative bridge artwork in pale lime and grey"></div>
</section>

</body>
</html>
```